Business card por a urban DJ, up scale audience target

Need a sober design, modern, conservative colors but i can consider some options, y play rnb, hip hop, EDM and top40.

Business card for contact and personal info, double sided, use logo attrached please; im 42 so i need a card acording to my age an target audience.

Target Market(s)

Adult people, up scale audience

Industry/Entity Type

Music Download

Contact Information for Business Card

Cel (574) 3209415586 www.lumaverso.com

Requirements
Must have
• open mind
Nice to have
• open mind
Should not have
• DJ

```html
<!DOCTYPE html>
<html lang="en">
<head>
<meta charset="utf-8">
<title>Lumaverso Business Card</title>
<link href="https://fonts.googleapis.com/css2?family=Noto+Sans:wght@400;700&display=swap" rel="stylesheet">
<style>
  :root {
    --ink: #2b2a29;
    --paper: #ffffff;
    --backdrop: #ebe5da;
    --card-shadow: rgba(0, 0, 0, 0.18);
  }
  * { margin: 0; padding: 0; box-sizing: border-box; }
  html, body {
    width: 1189px; height: 1200px; overflow: hidden;
    background: var(--backdrop);
    font-family: "Noto Sans", Arial, sans-serif;
    color: var(--ink);
  }
  .canvas { position: relative; width: 1189px; height: 1200px; }
  .card {
    position: absolute; left: 171px; width: 855px; height: 488px;
    box-shadow: 0 4px 12px var(--card-shadow);
  }
  .card--front { top: 67px; background: var(--paper); }
  .card--back { top: 627px; background: var(--ink); color: var(--paper); }

  .brand { position: absolute; display: flex; align-items: center; gap: 16px; font-weight: 700; letter-spacing: 2px; line-height: 1; }
  .brand__square { width: 36px; height: 36px; background: currentColor; flex: none; }
  .card--front .brand { left: 44px; top: 92px; font-size: 60px; color: var(--ink); }

  .identity { position: absolute; right: 44px; top: 250px; text-align: right; }
  .identity__name { font-size: 31px; font-weight: 700; line-height: 1.1; letter-spacing: 0.5px; }
  .identity__title { font-size: 21px; font-weight: 400; line-height: 1.2; }
  .rule { position: absolute; left: 44px; top: 294px; width: 522px; height: 3px; background: var(--ink); }

  .contacts { position: absolute; left: 44px; top: 368px; list-style: none; }
  .contacts li { display: flex; align-items: center; gap: 9px; font-size: 21px; height: 30px; }
  .contacts svg { width: 24px; height: 24px; flex: none; }

  .address { position: absolute; right: 44px; top: 395px; text-align: right; font-size: 21px; line-height: 29px; }

  .card--back .brand { left: 50%; top: 190px; transform: translateX(-50%); font-size: 64px; color: var(--paper); }
  .back-url { position: absolute; left: 0; right: 0; top: 418px; text-align: center; font-size: 22px; }
</style>
</head>
<body>
<div class="canvas">
  <section class="card card--front">
    <div class="brand"><span class="brand__square"></span>LUMAVERSO</div>

    <div class="identity">
      <p class="identity__name">EMPLOYEE NAME</p>
      <p class="identity__title">Development Manager</p>
    </div>
    <div class="rule"></div>

    <ul class="contacts">
      <li>
        <svg viewBox="0 0 24 24" aria-hidden="true"><rect width="24" height="24" fill="#2b2a29"/><rect x="7.5" y="3.5" width="9" height="17" rx="1.5" fill="none" stroke="#fff" stroke-width="1.6"/><rect x="9.5" y="6" width="5" height="5" fill="#fff"/><circle cx="12" cy="17" r="1.2" fill="#fff"/></svg>
        (574) 3209415586
      </li>
      <li>
        <svg viewBox="0 0 24 24" aria-hidden="true"><rect width="24" height="24" fill="#2b2a29"/><rect x="4" y="6.5" width="16" height="11" fill="none" stroke="#fff" stroke-width="1.6"/><path d="M4 6.5l8 6.5 8-6.5M4 17.5l6-5.5M20 17.5l-6-5.5" fill="none" stroke="#fff" stroke-width="1.4"/></svg>
        hello@lumaverso.com
      </li>
      <li>
        <svg viewBox="0 0 24 24" aria-hidden="true"><rect width="24" height="24" fill="#2b2a29"/><circle cx="12" cy="12" r="7.5" fill="none" stroke="#fff" stroke-width="1.4"/><ellipse cx="12" cy="12" rx="3.2" ry="7.5" fill="none" stroke="#fff" stroke-width="1.2"/><path d="M4.5 12h15M6 8h12M6 16h12" stroke="#fff" stroke-width="1.1"/></svg>
        www.lumaverso.com
      </li>
    </ul>

    <address class="address" style="font-style: normal;">
      P.O. Box 418, Harbour Lane<br>
      Westmere Bay, Auckland
    </address>
  </section>

  <section class="card card--back">
    <div class="brand"><span class="brand__square"></span>LUMAVERSO</div>
    <p class="back-url">www.lumaverso.com</p>
  </section>
</div>
</body>
</html>
```